BRIX Rentals ( Website Graphic design ) small property management new business ( real estate )

I need a website designed for a new small Property Management ( no sales ) company I'm starting up soon. I have a design in mind that I like and would like to keep it quite similar to this if possible using my logo and colour scheme and slightly ALTER the layout. and maybe a little more interactive with some motion and images etc
Please see the link to show the simplicity I'm after. I want to be bold ad very clear and concise. I love the simplicity of this design but not necessarily the pages with just text on them. I would want them to be a bit more interesting with some pictures and photos. http://www.lindavostrel.com.au/

The branding on the site should be bold and very sharp.

My target market is the mid to high end of the rental market in Darwin Australia and should reflect "good quality, outstanding service and attention to detail, energetic, integrity, "

I will only require a few pages to start with, Home / Company Profile / Management Services / Owners information / Tenant information / Properties and About Darwin. I will be able to provide text for each of the pages but would be no more than 4-6 paragraphs apart from the management services page which would detail a number of the services we would offer. The properties page will just be a link to homelistz,com.au to show my listings and then a couple more links to owner and tenant portals, chatterbox page etc. It must also be responsive to mobile devices.

I would also like to include a chatterbox page design and build.

regards
Marta Penhale

Target Market(s)

property owners, investors, Darwin Australia, renters, ages 30 - 60, tenants

Industry/Entity Type

Property Management

Font styles to use
Other font styles liked:
• i like helvetica, but not essential

Requirements
Must have
• Clean and crisp pages, not busy , responsive to devices
• links to portals and chatterbox, any ability to add other links at a later date.
Nice to have
• music - must be upbeat but not over the top
Should not have
• be too busy on each page

```html
<!DOCTYPE html>
<html lang="en">
<head>
<meta charset="utf-8">
<title>BRIX Rentals – Home</title>
<link rel="stylesheet" href="https://fonts.googleapis.com/css2?family=Open+Sans:wght@400;600&display=swap">
<style>
  :root {
    --bg: #000000;
    --teal: #11898f;
    --teal-2: #4f9ca2;
    --teal-3: #7aaeb3;
    --teal-4: #a6c6cc;
    --white: #ffffff;
    --ink: #3a3a3a;
  }
  html, body {
    margin: 0;
    padding: 0;
    overflow: hidden;
    background: var(--bg);
  }
  .canvas {
    position: relative;
    width: 1200px;
    height: 900px;
    background: var(--bg);
    overflow: hidden;
    font-family: "Open Sans", Arial, sans-serif;
  }
  .nav-home {
    position: absolute;
    left: 414px;
    top: 0;
    width: 371px;
    height: 63px;
    background: var(--teal);
    color: var(--white);
    font-size: 42px;
    line-height: 63px;
    text-align: center;
    letter-spacing: 1px;
    text-decoration: none;
  }
  .nav-feedback {
    position: absolute;
    left: 0;
    top: 275px;
    width: 63px;
    height: 350px;
    background: var(--teal);
    color: var(--white);
    font-size: 38px;
    letter-spacing: 1px;
    display: flex;
    align-items: center;
    justify-content: center;
    text-decoration: none;
  }
  .nav-feedback span,
  .page-tab span {
    writing-mode: vertical-rl;
    transform: rotate(180deg);
    white-space: nowrap;
  }
  .footer-band {
    position: absolute;
    left: 0;
    bottom: 0;
    width: 1200px;
    height: 49px;
    background: var(--teal);
  }
  .page-stack {
    position: absolute;
    left: 219px;
    top: 275px;
    width: 762px;
    height: 348px;
  }
  .page-tab {
    position: absolute;
    top: 0;
    left: 0;
    height: 348px;
    border-radius: 0 26px 26px 0;
    color: var(--white);
    font-size: 21px;
    text-decoration: none;
  }
  .page-tab span {
    position: absolute;
    top: 0;
    bottom: 0;
    width: 53px;
    display: flex;
    align-items: center;
    justify-content: center;
  }
  .tab-profile  { width: 604px; background: var(--teal);   z-index: 4; }
  .tab-services { width: 656px; background: var(--teal-2); z-index: 3; }
  .tab-owners   { width: 709px; background: var(--teal-3); z-index: 2; }
  .tab-profile-alt { width: 762px; background: var(--teal-4); z-index: 1; }
  .tab-profile span  { left: 551px; }
  .tab-services span { left: 604px; }
  .tab-owners span   { left: 656px; }
  .tab-profile-alt span { left: 709px; }
  .home-card {
    position: absolute;
    left: 0;
    top: 0;
    width: 551px;
    height: 348px;
    background: var(--white);
    border-radius: 26px;
    z-index: 5;
    display: flex;
    align-items: center;
    justify-content: center;
  }
  .brand-name {
    margin: 0;
    color: var(--teal);
    font-size: 64px;
    font-weight: 400;
    letter-spacing: 1px;
  }
</style>
</head>
<body>
  <main class="canvas">
    <a class="nav-home" href="#home">Home</a>
    <a class="nav-feedback" href="#feedback"><span>Feedback</span></a>

    <section class="page-stack">
      <div class="home-card">
        <h1 class="brand-name">BRIX Rentals</h1>
      </div>
      <a class="page-tab tab-profile" href="#company-profile"><span>Company Profile</span></a>
      <a class="page-tab tab-services" href="#management-services"><span>Management Services</span></a>
      <a class="page-tab tab-owners" href="#owners-information"><span>Owners information</span></a>
      <a class="page-tab tab-profile-alt" href="#company-profile-more"><span>Company Profile</span></a>
    </section>

    <footer class="footer-band"></footer>
  </main>
</body>
</html>
```